" Assessoria e consultoria de projetos agropecuários com foco em bovinos. DIFERENCIAIS ? Atendimento personalizado; ? Foco em processos; Melhoria continua - metodologia LEAN ? Foco no cliente e na qualidade do serviço; ? Acompanhamento dos resultados gerados pela consultoria; ? Serviço com conhecimento agregado. Atendimento personalizado: A Brota enxerga a necessidade do contato personalizado com o cliente, demonstrando constantemente que a empresa está interessada em ajudá-lo e trazer soluções para seus problemas. ? Foco em processos: Como a maioria das empresas que prestam consultoria na área estão mais voltadas para TÉCNICAS animal, o foco em processos e gestao por processos torna-se um diferencial da Brota. A empresa poderia aproveitar essa vantagem divulgando a importância do gerenciamento eficaz nas fazendas através dos processos agropecuários. ? Foco no cliente e na qualidade do serviço: Através do atendimento personalizado, o consultor da Brota tem a responsabilidade de manter o comprometimento com o cliente e com a qualidade dos serviços entregues. Assim, a empresa cria uma boa relação com os consumidores, fidelizando-os. ? Acompanhamento dos resultados gerados pela consultoria: Além de prestar consultoria, a Empresa auxilia o cliente a implementar as técnicas e soluções, fazendo o acompanhamento de resultados com indicadores. ? Serviço com maior valor agregado: Através da constante busca por conhecimento na área, a qualidade dos projetos entregues será cada vez maior, consequentemente tornando-os mais eficazes e eficientes. "

```html
<!DOCTYPE html>
<html lang="pt-BR">
<head>
<meta charset="UTF-8">
<title>Brota – Cartões de visita</title>
<link href="https://fonts.googleapis.com/css2?family=Montserrat:wght@300;400;600;700&display=swap" rel="stylesheet">
<style>
  :root{
    --page:#e9eaec;
    --navy-deep:#0a1836;
    --navy-mid:#1b3566;
    --green:#3aae5a;
    --green-light:#8fd6a0;
    --ink:#14244a;
    --grey-text:#5b6475;
    --silver:#dfe2e7;
    --white:#ffffff;
  }
  *{margin:0;padding:0;box-sizing:border-box}
  html,body{width:1200px;height:1200px;overflow:hidden}
  body{
    background:var(--page);
    font-family:"Montserrat",sans-serif;
    display:flex;flex-direction:column;align-items:center;justify-content:center;gap:64px;
  }
  .card{
    width:900px;height:514px;position:relative;overflow:hidden;
    border-radius:6px;box-shadow:0 10px 30px rgba(10,24,54,.18);
  }
  .card-front{
    background:radial-gradient(ellipse at 45% 40%,var(--navy-mid) 0%,var(--navy-deep) 75%);
  }
  .card-back{background:var(--white)}
  .corner-band{position:absolute;right:0;bottom:0;width:900px;height:514px}

  .brand{
    position:absolute;left:50%;top:46%;transform:translate(-50%,-50%);
    display:flex;flex-direction:column;align-items:center;gap:14px;
  }
  .brand-mark{
    width:74px;height:74px;border-radius:50%;background:var(--silver);
  }
  .brand-name{
    color:var(--white);font-weight:300;font-size:70px;letter-spacing:.28em;
    text-transform:uppercase;line-height:1;margin-right:-.28em;
  }
  .brand-tagline{
    color:var(--silver);font-weight:400;font-size:14px;letter-spacing:.32em;text-transform:uppercase;
  }

  .holder{position:absolute;left:70px;top:150px}
  .holder-name{color:var(--ink);font-weight:700;font-size:34px;letter-spacing:.02em;text-transform:uppercase}
  .holder-role{color:var(--grey-text);font-size:16px;margin-top:4px;letter-spacing:.05em}
  .contacts{
    position:absolute;left:70px;top:270px;list-style:none;
    display:grid;grid-template-columns:auto auto;column-gap:36px;row-gap:14px;
    color:var(--grey-text);font-size:16px;
  }
  .contacts li{display:flex;align-items:center;gap:10px}
  .contacts .wide{grid-column:1 / span 2}
  .contacts svg{width:18px;height:18px;flex:none}
  .back-watermark{
    position:absolute;right:-40px;top:70px;
    color:var(--silver);font-weight:300;font-size:190px;letter-spacing:.06em;
    text-transform:uppercase;line-height:1;
  }
</style>
</head>
<body>

<section class="card card-front" aria-label="Frente do cartão">
  <svg class="corner-band" viewBox="0 0 900 514" aria-hidden="true">
    <defs>
      <linearGradient id="greenBand" x1="0" x2="1">
        <stop offset="0" stop-color="#8fd6a0"/>
        <stop offset="1" stop-color="#3aae5a"/>
      </linearGradient>
    </defs>
    <path d="M560 514 L900 380 L900 396 L600 514 Z" fill="#ffffff" opacity=".12"/>
    <path d="M640 514 L900 412 L900 514 Z" fill="url(#greenBand)"/>
  </svg>
  <div class="brand">
    <div class="brand-mark"></div>
    <div class="brand-name">Brota</div>
    <div class="brand-tagline">Processos agropecuários</div>
  </div>
</section>

<section class="card card-back" aria-label="Verso do cartão">
  <div class="back-watermark">Brota</div>
  <svg class="corner-band" viewBox="0 0 900 514" aria-hidden="true">
    <defs>
      <linearGradient id="greenBandBack" x1="0" x2="1">
        <stop offset="0" stop-color="#8fd6a0"/>
        <stop offset="1" stop-color="#3aae5a"/>
      </linearGradient>
    </defs>
    <path d="M640 514 L900 412 L900 514 Z" fill="url(#greenBandBack)"/>
  </svg>

  <div class="holder">
    <div class="holder-name">Nome Sobrenome</div>
    <div class="holder-role">Cargo</div>
  </div>

  <ul class="contacts">
    <li>
      <svg viewBox="0 0 24 24"><path d="M6.6 10.8a15 15 0 006.6 6.6l2.2-2.2a1 1 0 011-.25 11.4 11.4 0 003.6.57 1 1 0 011 1V20a1 1 0 01-1 1A17 17 0 013 4a1 1 0 011-1h3.5a1 1 0 011 1c0 1.25.2 2.45.57 3.57a1 1 0 01-.25 1z" fill="#3aae5a"/></svg>
      (11) 90000-1234
    </li>
    <li>
      <svg viewBox="0 0 24 24"><path d="M6.6 10.8a15 15 0 006.6 6.6l2.2-2.2a1 1 0 011-.25 11.4 11.4 0 003.6.57 1 1 0 011 1V20a1 1 0 01-1 1A17 17 0 013 4a1 1 0 011-1h3.5a1 1 0 011 1c0 1.25.2 2.45.57 3.57a1 1 0 01-.25 1z" fill="#3aae5a"/></svg>
      (11) 3000-4567
    </li>
    <li class="wide">
      <svg viewBox="0 0 24 24"><path d="M12 2a7 7 0 00-7 7c0 5.2 7 13 7 13s7-7.8 7-13a7 7 0 00-7-7zm0 9.5A2.5 2.5 0 1112 6.5a2.5 2.5 0 010 5z" fill="#3aae5a"/></svg>
      Rua das Palmeiras, 120 - Centro - SP
    </li>
    <li>
      <svg viewBox="0 0 24 24"><path d="M3 5h18v14H3z" fill="none" stroke="#3aae5a" stroke-width="2"/><path d="M3 6l9 7 9-7" fill="none" stroke="#3aae5a" stroke-width="2"/></svg>
      contato@brota.com
    </li>
    <li>
      <svg viewBox="0 0 24 24"><rect x="3" y="3" width="18" height="18" rx="3" fill="#3aae5a"/></svg>
      /brota
    </li>
  </ul>
</section>

</body>
</html>
```